Business Card for Web Design consulting firm

Business card designs for Web Design consulting firm

Target Market(s)

English speaking adults ages 30 - 60. Predominantly professional services eg. Doctor, Dentist

Industry/Entity Type

Consulting

Requirements
Must have
• Double sided card

```html
<!DOCTYPE html>
<html lang="en">
<head>
<meta charset="utf-8">
<title>Lumenta Business Cards</title>
<link rel="stylesheet" href="https://fonts.googleapis.com/css2?family=Jost:wght@400;500;600;700&display=swap">
<style>
:root{
  --orange:#f39a27;
  --charcoal:#4b4b4b;
  --paper:#ffffff;
  --bg:#ffffff;
  --faint:rgba(255,255,255,0.14);
}
*{margin:0;padding:0;box-sizing:border-box}
html,body{width:1200px;height:1200px;overflow:hidden;background:var(--bg);font-family:'Jost',sans-serif}
.sheet{position:relative;width:1200px;height:1200px}
.card{position:absolute;width:290px;height:174px;border-radius:7px;background:var(--paper);overflow:hidden;box-shadow:0 2px 6px rgba(0,0,0,.35)}
.card.tall{width:174px;height:290px}
.card.dark{background:var(--charcoal)}
.wordmark{display:flex;align-items:center;gap:6px;color:var(--charcoal);font-weight:600;letter-spacing:2px;line-height:1}
.wordmark .dot{width:12px;height:12px;background:var(--orange)}
.wordmark.lg{font-size:22px}
.wordmark.md{font-size:17px}
.wordmark.sm{font-size:13px}
.wordmark.sm .dot{width:9px;height:9px}
.center{position:absolute;left:0;right:0;display:flex;flex-direction:column;align-items:center}
.tagline{color:var(--orange);font-size:7px;font-weight:500;letter-spacing:.3px}
.name{color:var(--charcoal);font-weight:700;font-size:11px;letter-spacing:.5px}
.addr{color:var(--orange);font-size:8px;line-height:1.3}
.band{position:absolute;left:0;right:0;background:var(--orange);color:#fff;font-size:8px;font-weight:600;text-align:center}
.panel{position:absolute;top:0;bottom:0;right:0;width:44%}
.panel .name{position:absolute;right:10px;top:10px}
.panel .role{position:absolute;right:10px;top:23px;color:#fff;font-size:8px}
.panel .foot{position:absolute;right:10px;bottom:8px;font-size:6px;font-weight:600}
.ghost{position:absolute;background:var(--faint);border-radius:3px}
</style>
</head>
<body>
<div class="sheet">

  <!-- Set 1 -->
  <div class="card" style="left:334px;top:25px">
    <div class="center" style="top:74px"><div class="wordmark lg"><span class="dot"></span>LUMENTA</div></div>
  </div>
  <div class="card" style="left:643px;top:25px">
    <div class="center" style="top:22px;gap:6px">
      <div class="wordmark md"><span class="dot"></span>LUMENTA</div>
      <div class="tagline">TAGLINE HERE</div>
    </div>
    <div class="center" style="top:86px"><div class="name">JOHN DOE</div></div>
    <div class="center addr" style="top:120px"><span>174 Harbor Lane Street</span><span>Fairview, CA 90415</span><span>415 7720 3184</span></div>
  </div>

  <!-- Set 2 -->
  <div class="card" style="left:334px;top:230px">
    <div class="center" style="top:74px"><div class="wordmark lg"><span class="dot"></span>LUMENTA</div></div>
  </div>
  <div class="card" style="left:643px;top:230px">
    <div style="position:absolute;left:42px;top:68px;display:flex;flex-direction:column;align-items:center;gap:5px">
      <div class="wordmark sm"><span class="dot"></span>LUMENTA</div>
      <div class="tagline" style="color:var(--orange)">TAGLINE HERE</div>
    </div>
    <div style="position:absolute;left:158px;top:62px">
      <div class="name">JOHN DOE</div>
      <div class="addr" style="font-size:7px;margin-top:2px">174 Harbor Lane Street<br>Fairview, CA 90415<br>415 7720 3184</div>
    </div>
    <div class="band" style="bottom:0;height:17px;line-height:17px">WEB DESIGN CONSULTING</div>
  </div>

  <!-- Set 3 -->
  <div class="card" style="left:334px;top:431px">
    <div class="center" style="top:74px"><div class="wordmark lg"><span class="dot"></span>LUMENTA</div></div>
  </div>
  <div class="card" style="left:643px;top:431px">
    <div style="position:absolute;left:14px;top:14px"><div class="wordmark sm"><span class="dot"></span>LUMENTA</div></div>
    <div class="addr" style="position:absolute;left:14px;bottom:12px;font-size:7px">174 Harbor Lane Street<br>Fairview, CA 90415<br>415 7720 3184</div>
    <div class="panel" style="background:var(--orange)">
      <div class="name" style="font-size:10px">JOHN DOE</div>
      <div class="role">Managing Director</div>
      <div class="ghost" role="img" aria-label="Faint brand square" style="right:40px;top:80px;width:34px;height:24px"></div>
      <div class="foot" style="color:var(--charcoal)">WEB DESIGN CONSULTING</div>
    </div>
  </div>

  <!-- Set 4 -->
  <div class="card dark" style="left:334px;top:629px">
    <div style="position:absolute;left:111px;top:51px;width:177px;height:73px;background:var(--paper);display:flex;align-items:center;justify-content:center">
      <div class="wordmark md"><span class="dot"></span>LUMENTA</div>
    </div>
  </div>
  <div class="card" style="left:643px;top:629px">
    <div style="position:absolute;left:14px;top:20px"><div class="wordmark md"><span class="dot"></span>LUMENTA</div></div>
    <div class="addr" style="position:absolute;left:14px;bottom:12px;font-size:7px">174 Harbor Lane Street<br>Fairview, CA 90415<br>415 7720 3184</div>
    <div class="panel" style="background:var(--charcoal)">
      <div class="name" style="font-size:10px;color:var(--orange)">JOHN DOE</div>
      <div class="role">Managing Director</div>
      <div class="ghost" role="img" aria-label="Faint brand square" style="right:40px;top:80px;width:34px;height:24px"></div>
      <div class="foot" style="color:var(--orange)">WEB DESIGN CONSULTING</div>
    </div>
  </div>

  <!-- Set 5 vertical -->
  <div class="card tall dark" style="left:405px;top:835px">
    <div class="ghost" role="img" aria-label="Faint brand square" style="left:30px;top:40px;width:60px;height:60px;background:rgba(255,255,255,0.08)"></div>
    <div style="position:absolute;left:0;right:0;top:177px;height:67px;background:var(--paper);display:flex;align-items:center;justify-content:center">
      <div class="wordmark md"><span class="dot"></span>LUMENTA</div>
    </div>
  </div>
  <div class="card tall dark" style="left:661px;top:835px">
    <div style="position:absolute;left:0;right:0;top:0;height:93px;background:var(--paper);display:flex;align-items:center;justify-content:center">
      <div class="wordmark md"><span class="dot"></span>LUMENTA</div>
    </div>
    <div class="band" style="top:93px;height:22px;line-height:22px;font-size:7px;font-weight:500">TAGLINE HERE</div>
    <div class="center" style="top:162px"><div class="name" style="color:var(--orange);font-size:15px">JOHN DOE</div></div>
    <div class="center" style="top:240px;color:#fff;font-size:9px;line-height:1.3"><span>174 Harbor Lane Street</span><span>Fairview, CA 90415</span><span>415 7720 3184</span></div>
  </div>

</div>
</body>
</html>
```